Consulting firm needs a professional letterhead design

We need a professional letterhead design which is simple but unique. It should carry attributes of the latest designs in the market suitable for professional environmental consultancies.

- The logo is attached for you to USE.
- Our preferred color scheme is that shown in the logo.
- Letterhead text color is your choice to make.
- Logo to the left and text to the right plus slogan/tagline is desirable for this letterhead.

Use any address etc. of your choice in the letterhead.

Target Market(s)

Consulting firms and government agencies

Industry/Entity Type

Environmental Consultant

Colors
acd037
fece3e
85cae6
3277b5

Requirements
Must have
• Logo supplied and color scheme must be used.
Nice to have
• Nexa font is used in the Logo, so it would ne nice to have nexa font in the letterhead too.

```html
<!DOCTYPE html>
<html lang="en">
<head>
<meta charset="utf-8">
<title>Terraven Letterhead</title>
<link href="https://fonts.googleapis.com/css2?family=Mulish:wght@300;400;600;700&family=Parisienne&display=swap" rel="stylesheet">
<style>
  :root {
    --blue: #1380a4;
    --orange: #f5861f;
    --green: #16a04a;
    --ink: #4a4a55;
    --brand-ink: #3b3f5c;
    --paper: #ffffff;
  }
  * { margin: 0; padding: 0; box-sizing: border-box; }
  html, body { width: 949px; height: 1200px; overflow: hidden; background: var(--paper); }
  .letterhead {
    position: relative; width: 949px; height: 1200px;
    font-family: "Mulish", sans-serif; color: var(--ink); background: var(--paper);
  }
  .brand { position: absolute; left: 56px; top: 86px; display: flex; align-items: center; gap: 12px; }
  .brand-dot { width: 86px; height: 86px; border-radius: 50%; background: var(--blue); }
  .brand-name { font-weight: 700; font-size: 34px; letter-spacing: 1.5px; color: var(--brand-ink); line-height: 1; }
  .brand-tagline { font-size: 14px; font-weight: 600; color: var(--brand-ink); margin-top: 2px; letter-spacing: 0.2px; }
  .contact {
    position: absolute; right: 57px; top: 84px; text-align: right;
    font-size: 14.5px; line-height: 22px; font-weight: 400; letter-spacing: 0.2px;
  }
  .contact .address { line-height: 18px; margin-bottom: 4px; }
  .contact-row { display: flex; justify-content: flex-end; align-items: center; gap: 8px; }
  .contact-row svg { width: 13px; height: 13px; }
  .side-tabs { position: absolute; right: 0; top: 69px; width: 13px; }
  .side-tabs span { display: block; height: 43px; }
  .recipient { position: absolute; left: 56px; top: 329px; font-size: 13.5px; line-height: 20px; letter-spacing: 0.2px; }
  .body-copy {
    position: absolute; left: 56px; top: 434px; width: 836px;
    font-size: 14px; font-weight: 300; line-height: 20px; letter-spacing: 0.3px; text-align: justify;
  }
  .body-copy p { margin-bottom: 27px; }
  .sign-label { position: absolute; left: 56px; top: 820px; font-size: 13.5px; }
  .sign-name { position: absolute; left: 56px; top: 842px; font-family: "Parisienne", cursive; font-size: 22px; color: var(--blue); }
  .footer-bands { position: absolute; left: 0; bottom: 0; width: 100%; height: 32px; display: flex; }
  .footer-bands span { flex: 1; }
  .blue { background: var(--blue); } .orange { background: var(--orange); } .green { background: var(--green); }
</style>
</head>
<body>
<div class="letterhead">
  <div class="brand">
    <div class="brand-dot"></div>
    <div>
      <div class="brand-name">TERRAVEN</div>
      <div class="brand-tagline">Turning evidence into sound choices</div>
    </div>
  </div>

  <div class="contact">
    <div class="address">42 Riverside Lane Kivu,<br>Suite 7, 30415</div>
    <div class="contact-row">+243 800 555 014
      <svg viewBox="0 0 16 16"><path fill="#1380a4" d="M3.5 1.5l2.5 0 1 3.5-1.6 1.2a8 8 0 0 0 4.4 4.4L11 9l3.5 1v2.5c0 1-1 2-2 2A11 11 0 0 1 1.5 3.5c0-1 1-2 2-2z"/></svg>
    </div>
    <div class="contact-row">contact@terraven.example
      <svg viewBox="0 0 16 16"><rect x="1.5" y="3.5" width="13" height="9" fill="none" stroke="#1380a4" stroke-width="1.2"/><path d="M1.5 3.5l6.5 5 6.5-5" fill="none" stroke="#1380a4" stroke-width="1.2"/></svg>
    </div>
    <div class="contact-row">www.terraven.example
      <svg viewBox="0 0 16 16" fill="none" stroke="#1380a4" stroke-width="1.1"><circle cx="8" cy="8" r="6.5"/><ellipse cx="8" cy="8" rx="3" ry="6.5"/><path d="M1.5 8h13M2.5 5h11M2.5 11h11"/></svg>
    </div>
  </div>

  <div class="side-tabs"><span class="green"></span><span class="orange"></span><span class="blue"></span></div>

  <div class="recipient">Mr/s<br>First Name and Last Name<br>Company Name<br>Address</div>

  <div class="body-copy">
    <p>Contrary to popular belief, Lorem Ipsum is not simply random text. It has roots in a piece of classical Latin literature from 45 BC, making it over 2000 years old. Daniel Ferrow, a Latin professor at Westbrook College in Virginia, looked up one of the more obscure Latin words, consectetur, from a Lorem Ipsum passage, and going through the cites of the word in classical literature, discovered the undoubtable source. Lorem Ipsum comes from sections 1.10.32 and 1.10.33 of "de Finibus Bonorum et Malorum" (The Extremes of Good and Evil) by Cicero, written in 45 BC. This book is a treatise on the theory of ethics, very popular during the Renaissance. The first line of Lorem Ipsum, "Lorem ipsum dolor sit amet.</p>
    <p>he standard chunk of Lorem Ipsum used since the 1500s is reproduced below for those interested. Sections 1.10.32 and 1.10.33 from "de Finibus Bonorum et Malorum" by Cicero are also reproduced in their exact original form, accompanied by English versions from the 1914 translation by H. Redford. Lorem ipsum dolor sit amet, consectetur adipiscing elit, sed do eiusmod tempor incididunt ut labore et dolore magna aliqua. Ut enim ad minim veniam, quis nostrud exercitation ullamco laboris nisi ut aliquip ex ea commodo consequat.</p>
    <p>It is a long established fact that a reader will be distracted by the readable content of a page when looking at its layout. The point of using Lorem Ipsum is that it has a more-or-less normal distribution of letters, as opposed to using 'Content here, content here', making it look like readable English. Many desktop publishing packages and web page editors now .</p>
  </div>

  <div class="sign-label">Signature</div>
  <div class="sign-name">Amara Keller</div>

  <div class="footer-bands"><span class="blue"></span><span class="orange"></span><span class="green"></span></div>
</div>
</body>
</html>
```